Qamra
قمرة كافيه
Hello Designers:-
Please check your e-mail inbox.
Thank you so much!
plz star rating...
The front and the back of the card should be one color "Beige". In front, it only shows the logo, the address, e-mail, twitter and instagram accounts. No need to type any other word like the word "قمرة"
As for the back, we want a loyalty card with 6 stamps with "Qamra" shape drawing on each. and the 6th qamra has a FREE written on it (Pic provided in brief)
If you have any comments, questions or requirements please do not hesitate to contact me on my e-mail or here, in the discussion.
Thank you so much for your work! :)
Hello designers: Please make sure to read the project brief as we want a (Double) sided business card/loyalty card. Moreover, please be aware that the card color should follow the color of the store "Beige" and not the logo color (Store pic provided in the brief)
Thank you so much for your effort! And good luck!

```html
<!DOCTYPE html>
<html lang="en">
<head>
<meta charset="utf-8">
<title>Qamra – Business &amp; Loyalty Card</title>
<link rel="stylesheet" href="https://fonts.googleapis.com/css2?family=Cairo:wght@400;700&family=Arimo:wght@400&display=swap">
<style>
  :root {
    --sheet: #ffffff;
    --sheet-frame: #8a8a8a;
    --beige: #c8ab84;
    --beige-deep: #8d6e4f;
    --card-edge: #a08a6c;
    --cream: #f7efe2;
    --ink-light: #ffffff;
    --ornament-glow: rgba(236, 224, 203, 0.75);
    --ornament-fade: rgba(200, 171, 132, 0);
    --band-tone: rgba(176, 146, 108, 0.7);
  }
  * { box-sizing: border-box; margin: 0; padding: 0; }
  html, body { width: 1200px; height: 721px; overflow: hidden; background: var(--sheet); }
  .sheet {
    position: relative; width: 1200px; height: 721px;
    border: 3px solid var(--sheet-frame); background: var(--sheet);
  }
  .card { position: absolute; overflow: hidden; border: 1px solid var(--card-edge); }
  .card--front { left: 307px; top: 19px; width: 492px; height: 331px; background: var(--beige); }
  .card--back-light { left: 46px; top: 380px; width: 530px; height: 312px; background: var(--beige); }
  .card--back-dark { left: 612px; top: 380px; width: 545px; height: 312px; background: var(--beige-deep); }

  .brand-mark {
    position: absolute; font-family: "Cairo", sans-serif; font-weight: 400;
    color: var(--cream); font-size: 44px; line-height: 1; white-space: nowrap;
  }
  .card--front .brand-mark { left: 30px; top: 78px; }
  .card--back-light .brand-mark, .card--back-dark .brand-mark {
    left: 50%; top: 62px; transform: translateX(-50%);
  }

  .contact {
    position: absolute; left: 36px; top: 226px; list-style: none;
    font-family: "Arimo", sans-serif; font-size: 12px; line-height: 18.5px; color: var(--ink-light);
  }
  .contact .address { font-family: "Cairo", sans-serif; font-size: 12px; direction: rtl; text-align: left; }
  .contact .social { display: flex; align-items: center; gap: 4px; }
  .contact .social i { display: inline-block; width: 10px; height: 10px; background: var(--cream); }

  .ornament {
    position: absolute; right: 0; top: 0; width: 120px; height: 300px;
    background: radial-gradient(ellipse at 55% 45%, var(--ornament-glow) 0%, var(--ornament-fade) 72%);
  }
  .corner-band {
    position: absolute; right: 0; bottom: 0; width: 230px; height: 70px;
    background: linear-gradient(to top left, var(--band-tone) 0%, var(--ornament-fade) 70%);
  }

  .loyalty-text {
    position: absolute; left: 0; width: 100%; text-align: center;
    font-family: "Arimo", sans-serif; font-size: 13px; color: var(--ink-light);
  }
  .loyalty-text--offer { top: 202px; }
  .loyalty-text--note { top: 268px; }
</style>
</head>
<body>
<main class="sheet">
  <section class="card card--front" aria-label="Card front">
    <div class="brand-mark">قمرة</div>
    <ul class="contact">
      <li class="address">مجمع الواحة التجاري - الطابق الثاني</li>
      <li>Phone: 555 301 72</li>
      <li>Email: QamraKuwait@qamramail.com</li>
      <li class="social"><i></i>@Qamra</li>
      <li class="social"><i></i>@QamraKuwait</li>
    </ul>
    <div class="ornament" role="img" aria-label="Decorative floral swirl ornament"></div>
    <div class="corner-band" role="img" aria-label="Decorative flowing swoosh ornament"></div>
  </section>

  <section class="card card--back-light" aria-label="Card back, beige">
    <div class="brand-mark">قمرة</div>
    <p class="loyalty-text loyalty-text--offer">Buy 5 and get the 6th refill for free</p>
    <p class="loyalty-text loyalty-text--note">(5 Shaped Qamra pictures and the 6th with a Free word on it)</p>
  </section>

  <section class="card card--back-dark" aria-label="Card back, brown">
    <div class="brand-mark">قمرة</div>
    <p class="loyalty-text loyalty-text--offer">Buy 5 and get the 6th refill for free</p>
    <p class="loyalty-text loyalty-text--note">(5 Shaped Qamra pictures and the 6th with a Free word on it)</p>
  </section>
</main>
</body>
</html>
```